Skyreach Pacific Aerial, a Sydney based startup need a visiting card designed

We are after a visiting card which is bold and eye catching. We are a drone company providing services and we are also Korvane authorized dealer who also sell consumer and industrial drones

Our website is under construction but you can excess from link below.

www.skyreachpacificaerial.com.au/test/

Feel free to contact me for any clarifications. we have given 5 days for the project but we are flexible to extend the project to 10 days.

Target Market(s)

Private and government organisation

Industry/Entity Type

Business Service

Contact Information for Business Card

Skyreach Pacific Aerial PTY LTD

Henrik Vollmer (Ned) ( Director)

17 Calloway Lane, Merrigum Flat, NSW 2571

Authorized Korvane Dealer

0471 238 905 / 1300Skyreachpa

info@skyreachpacificaerial.com.au

website: www.skyreachpacificaerial.com.au

Font styles to use
Serif

Requirements
Must have
• bold and stand out.
Nice to have
• colours complimenting the logo
Should not have
• not black card

```html
<!DOCTYPE html>
<html lang="en">
<head>
<meta charset="utf-8">
<title>Skyreach Pacific Aerial – Business Card</title>
<link href="https://fonts.googleapis.com/css2?family=Open+Sans:wght@400;700&display=swap" rel="stylesheet">
<style>
  :root {
    --backdrop: #e9e9e9;
    --paper: #f6f6f6;
    --navy: #0d2137;
    --gold: #f2ac00;
    --ink-soft: #6b6b6b;
  }
  * { margin: 0; padding: 0; box-sizing: border-box; }
  html, body { width: 1200px; height: 900px; overflow: hidden; }
  body {
    background: var(--backdrop);
    font-family: "Open Sans", sans-serif;
    position: relative;
  }
  .card {
    position: absolute;
    left: 382px;
    width: 412px;
    height: 248px;
    overflow: hidden;
  }
  .card--front { top: 150px; background: var(--paper); }
  .card--back { top: 476px; background: var(--navy); }

  .holder { position: absolute; left: 26px; top: 52px; }
  .holder__name {
    font-size: 17px; font-weight: 700; color: var(--navy); letter-spacing: 0.2px; line-height: 1.2;
  }
  .holder__role { font-size: 11.5px; color: var(--ink-soft); line-height: 1.3; }
  .divider { width: 11px; height: 1.5px; background: var(--navy); margin: 15px 0 0 2px; }

  .details {
    position: absolute; left: 27px; top: 132px;
    font-size: 11px; color: var(--ink-soft); line-height: 16.5px;
  }
  .details__block + .details__block { margin-top: 12px; }

  .brand {
    position: absolute;
    display: flex; flex-direction: column; align-items: center; gap: 6px;
    font-weight: 700; text-align: center; line-height: 1.15;
  }
  .brand__dot { border-radius: 50%; background: var(--gold); }
  .card--front .brand { left: 250px; top: 58px; width: 150px; color: var(--navy); font-size: 17px; }
  .card--front .brand__dot { width: 26px; height: 26px; }
  .card--back .brand { left: 106px; top: 56px; width: 200px; color: var(--gold); font-size: 24px; }
  .card--back .brand__dot { width: 34px; height: 34px; }

  .band { position: absolute; left: 0; bottom: 0; width: 412px; height: 13px; display: block; }
</style>
</head>
<body>

  <section class="card card--front" aria-label="Business card front">
    <div class="holder">
      <h1 class="holder__name">HENRIK VOLLMER</h1>
      <p class="holder__role">DIRECTOR</p>
      <div class="divider"></div>
    </div>

    <div class="details">
      <p class="details__block">17 Calloway Lane<br>Merrigum Flat, NSW 2571</p>
      <p class="details__block">0471 238 905 / 1300Skyreachpa<br>info@skyreachpacificaerial.com.au<br>www.skyreachpacificaerial.com.au</p>
    </div>

    <div class="brand">
      <span class="brand__dot"></span>
      <span class="brand__name">Skyreach Pacific Aerial</span>
    </div>

    <svg class="band" viewBox="0 0 412 13" preserveAspectRatio="none" aria-hidden="true">
      <polygon points="0,0 203,0 192,13 0,13" fill="var(--navy)"/>
      <polygon points="203,0 208,0 197,13 192,13" fill="#ffffff"/>
      <polygon points="208,0 412,0 412,13 197,13" fill="var(--gold)"/>
    </svg>
  </section>

  <section class="card card--back" aria-label="Business card back">
    <div class="brand">
      <span class="brand__dot"></span>
      <span class="brand__name">Skyreach Pacific Aerial</span>
    </div>

    <svg class="band" viewBox="0 0 412 13" preserveAspectRatio="none" aria-hidden="true">
      <polygon points="0,0 203,0 192,13 0,13" fill="var(--paper)"/>
      <polygon points="203,0 208,0 197,13 192,13" fill="var(--navy)"/>
      <polygon points="208,0 412,0 412,13 197,13" fill="var(--gold)"/>
    </svg>
  </section>

</body>
</html>
```